KeyBridge needs a modern business card

We are a modern conveyancing company and we need to appeal to the top (Multi-million dollar properties)and bottom on the property conveyancing market but our sweet spot is the middle of the market. I like professional with a hint of unconventional.

Target Market(s)

As above

Industry/Entity Type

Real Estate

Contact Information for Business Card

Back Of card:
thinking black with the logo and a tag line (I could be wrong about the black)
Tag line - Clear Guidance, Confident Closings

Front of Card:
Marissa Doyle (BBus (Finance) LLB)
Licensed Conveyancer
Email: marissa@keybridge.com.au

Key Bridge
ABN: 41 836 907
Suite 14, Level 3, 9 Harlow Avenue Westmead, NSW 2145
Phone: 1300 782 916

Sydney - Melbourne - Brisbane (Perhaps have this along the bottom of the card)

Requirements
Must have
• Sleek, modern and top end appeal (But approachable)
Should not have
• Not too cluttered

```html
<!DOCTYPE html>
<html lang="en">
<head>
<meta charset="utf-8">
<title>KeyBridge Business Card</title>
<link href="https://fonts.googleapis.com/css2?family=PT+Sans:wght@400;700&display=swap" rel="stylesheet">
<style>
  :root {
    --stage: #ecebe9;
    --card-white: #ffffff;
    --green-light: #9bd826;
    --green-dark: #5cb318;
    --green-text: #6cbd1c;
    --ink: #222222;
    --navy: #264f73;
    --sky-top: #1ecbff;
    --sky-bottom: #0f8ef4;
    --font: "PT Sans", Arial, sans-serif;
  }
  * { margin: 0; padding: 0; box-sizing: border-box; }
  html, body { width: 1200px; height: 900px; overflow: hidden; }
  body { background: var(--stage); font-family: var(--font); position: relative; }

  .card {
    position: absolute;
    border-radius: 14px;
    overflow: hidden;
    box-shadow: 0 6px 18px rgba(0,0,0,0.18);
  }

  /* Front */
  .card-front {
    left: 77px; top: 35px; width: 588px; height: 363px;
    background: var(--card-white);
    color: var(--ink);
  }
  .band-green {
    position: absolute; top: 40px; height: 98px;
    background: linear-gradient(180deg, var(--green-light), var(--green-dark));
  }
  .band-green.left { left: 0; width: 206px; }
  .band-green.right { left: 358px; width: 230px; }
  .front-brand {
    position: absolute; left: 206px; width: 152px; top: 74px;
    text-align: center; font-weight: 700; font-size: 26px; color: var(--navy);
  }
  .holder { position: absolute; left: 26px; top: 208px; }
  .holder-name { font-size: 22px; font-weight: 700; color: var(--green-text); line-height: 1.1; }
  .holder-name .quals { font-size: 15px; font-weight: 400; }
  .holder-role { font-size: 16px; margin-top: 2px; }
  .address { position: absolute; left: 26px; top: 268px; font-size: 16px; line-height: 1.5; }
  .details { position: absolute; right: 36px; top: 222px; text-align: right; font-size: 16px; line-height: 1.5; }
  .details .abn-label { color: var(--green-text); font-weight: 700; }
  .details .abn { margin-bottom: 14px; }
  .contact-line { display: flex; justify-content: flex-end; align-items: center; gap: 8px; }
  .contact-line svg { width: 12px; height: 12px; }
  .cities {
    position: absolute; left: 0; right: 0; bottom: 16px; text-align: center;
    font-size: 18px; font-weight: 700; color: var(--green-text);
  }

  /* Back */
  .card-back {
    left: 389px; top: 505px; width: 566px; height: 350px;
    background: linear-gradient(180deg, var(--sky-top), var(--sky-bottom));
    color: #ffffff;
  }
  .band-white { position: absolute; top: 82px; height: 96px; background: var(--card-white); }
  .band-white.left { left: 0; width: 202px; }
  .band-white.right { left: 370px; width: 196px; }
  .back-brand {
    position: absolute; left: 0; right: 0; top: 214px; text-align: center;
    font-size: 36px; font-weight: 400; color: #ffffff;
  }
  .tagline {
    position: absolute; left: 0; right: 0; top: 268px; text-align: center;
    font-size: 16px; font-weight: 700; letter-spacing: 0.3px; text-transform: uppercase;
  }
</style>
</head>
<body>
  <section class="card card-front">
    <div class="band-green left"></div>
    <div class="band-green right"></div>
    <div class="front-brand">KeyBridge</div>

    <div class="holder">
      <div class="holder-name">Marissa Doyle <span class="quals">(BBus (Finance) LLB)</span></div>
      <div class="holder-role">Licensed Conveyancer</div>
    </div>
    <div class="address">
      Suite 14, Level 3, 9 Harlow Avenue<br>Westmead, NSW 2145
    </div>
    <div class="details">
      <div class="abn"><span class="abn-label">ABN:</span> 41 836 907</div>
      <div class="contact-line">1300 782 916
        <svg viewBox="0 0 12 12" aria-hidden="true"><path fill="#6cbd1c" d="M2.4 0.6l1.8 0 0.8 2.6-1.2 1c0.6 1.4 1.6 2.4 3 3l1-1.2 2.6 0.8 0 1.8c0 0.6-0.5 1.1-1.1 1.1C4.7 9.7 1.3 6.3 1.3 1.7c0-0.6 0.5-1.1 1.1-1.1z"/></svg>
      </div>
      <div class="contact-line">marissa@keybridge.com.au
        <svg viewBox="0 0 12 12" aria-hidden="true"><rect x="0.5" y="2" width="11" height="8" fill="#6cbd1c"/><path d="M0.8 2.4L6 6.6l5.2-4.2" fill="none" stroke="#fff" stroke-width="1"/></svg>
      </div>
    </div>
    <div class="cities">Sydney - Melbourne - Brisbane</div>
  </section>

  <section class="card card-back">
    <div class="band-white left"></div>
    <div class="band-white right"></div>
    <div class="back-brand">KeyBridge</div>
    <div class="tagline">Clear Guidance, Confident Closings</div>
  </section>
</body>
</html>
```